Wordpress Design For Financial Investment Company

//** NEW WIREFRAME ADDED TO HELP WITH LAYOUT ISSUES. PLEASE REFER TO WIREFRAME IN ATTACHED FILES. NO DESIGN WILL BE CONSIDERED IF IT DOES NOT FOLLOW THE WIREFRAME. **//
//** PLEASE READ THE ENTIRE BRIEF INCLUDING ALL UPDATES TO THE BRIEF. THE CLIENT IS VERY SPECIFIC ABOUT WHAT THEY WANT AND I'VE COVERED SEVERAL THINGS IN THE UPDATES. THERE IS ALSO A VIDEO UPDATE THAT HAS SOME VALUABLE INFORMATION IN IT FOR THIS CONTEST. **//
The client is an investment advisor who needs a new website designed. The current site is http://www.velmorfield.net.
The client wants the site to be green to match the attached logo.
The home page should have relevant images in the rotator. No people hugging! This is a financial investment site, not a family counseling site.
Also, the client wants 4 buttons on the home page to highlight the 4 main areas they focus on:
Investment Advice and Education
General Financial Planning
Retirement Planning
401K Planning
The top right area of the site needs to have their phone number, a call to action, and 2 buttons.
Their phone number is 303-418-7639
The call to action should say something like "Call for a free consultation!"
The buttons need to say:
Login To Your Bluvexa Account
Login To Your Quillbrook Account
The final design should communicate professionalism, financial safety and growth.
Main navigation should be:
Home
About Us
Associates
Services
Contact
Mission Statement (Could also be "Our Mission")
This is a site that the client likes: http://www.pwkinvestmentconsulting.com/
Updates
The designs should not have:
Newsletter content. A newsletter sign up is fine
Learning Center
Calculators
Stock prices/tickers
The design should have a contact form on the page.
I have talked to my client and have some updates. I did a video update because I thought it would be easier to show what I'm trying to get across.
Reason: I am going to be extending the contest a few more days. I'm still not getting quite what I want and very few people are even trying to follow the creative brief and the updates to it.
PLEASE read the entire brief and the updates. There is also a video I made that explains everything. I've also attached a wireframe.
Thanks!
Target Market(s)
People looking for a high-end financial investment company.
Industry/Entity Type
Investment
Requirements
Must have
- !!FOLLOW THE WIREFRAME FOR LAYOUT!!
!!THEIR LOGO!!
4 buttons to highlight their main practice areas
Phone number in the top right
"Free Consultation" call to action
2 Login buttons in the top right
A contact form on the page.
Should not have
- The designs should not have:
Learning Center
Calculators
Stock prices/tickers

```html
<!DOCTYPE html>
<html lang="en">
<head>
<meta charset="utf-8">
<title>Velmorfield Financial Group</title>
<link rel="stylesheet" href="https://fonts.googleapis.com/css2?family=Oswald:wght@400;500&family=Arimo:wght@400;700&family=Lora:ital@1&display=swap">
<style>
:root{
  --green:#3f8a2e;
  --green-dark:#2c6a1f;
  --green-light:#6fb13c;
  --teal:#2e7d6b;
  --ink:#3a3a3a;
  --muted:#6a6a6a;
  --page:#ffffff;
  --header-bg:#ececec;
  --panel:#f3f3ef;
  --form-bg:#dfe9d6;
  --footer:#1f1f1f;
  --rule:#d4d4d4;
}
*{box-sizing:border-box;margin:0;padding:0}
html,body{width:898px;height:1200px;overflow:hidden}
body{background:var(--page);font-family:"Arimo",Arial,sans-serif;color:var(--ink);position:relative}
.header{position:absolute;left:0;top:0;width:898px;height:190px;background:linear-gradient(#f4f4f4,var(--header-bg))}
.nav{position:absolute;left:30px;top:70px;display:flex;gap:4px}
.nav a{display:block;padding:8px 14px;background:linear-gradient(var(--green-light),var(--green));color:#fff;font-size:13px;text-decoration:none;border-radius:6px 6px 0 0;border:1px solid var(--green-dark)}
.brand{position:absolute;left:385px;top:6px;width:130px;height:130px;border-radius:50%;background:#fff;border:3px solid var(--green);display:flex;align-items:center;justify-content:center;flex-direction:column}
.brand span{font-family:"Oswald",sans-serif;font-size:20px;color:var(--green-dark);letter-spacing:1px}
.contact{position:absolute;left:560px;top:10px;display:flex;align-items:center;gap:10px}
.contact .cta{font-size:13px;font-weight:700;color:var(--ink);line-height:1.2}
.contact .phone{font-family:"Oswald",sans-serif;font-size:30px;color:var(--green);letter-spacing:1px}
.logins{position:absolute;left:700px;top:125px;display:flex;gap:14px}
.login{display:flex;align-items:center;gap:4px}
.login i{width:24px;height:24px;border-radius:50%;background:var(--green);display:block}
.login a{background:var(--green);color:#fff;font-size:11px;padding:5px 10px;border-radius:3px;text-decoration:none}
.tagline{position:absolute;left:0;top:160px;width:898px;text-align:center;font-family:"Lora",serif;font-style:italic;font-size:14px;color:var(--muted)}
.slider{position:absolute;left:24px;top:192px;width:850px;height:290px;background:#f6f6f4;border:1px solid var(--rule)}
.slide-photo{position:absolute;left:0;top:0;width:390px;height:288px;background:linear-gradient(120deg,#e9ecef,#c9ced3 60%,#a9b0b6)}
.slide-title{position:absolute;left:410px;top:28px;font-family:"Oswald",sans-serif;font-size:33px;color:var(--green);font-weight:500}
.slide-text{position:absolute;left:410px;top:90px;width:410px;font-family:"Oswald",sans-serif;font-size:14px;line-height:1.75;color:var(--teal);text-transform:uppercase}
.dots{position:absolute;left:380px;top:258px;display:flex;gap:6px}
.dots span{width:20px;height:18px;background:#fff;border:1px solid var(--rule);font-size:10px;text-align:center;line-height:16px}
.areas{position:absolute;left:24px;top:495px;width:850px;display:flex;gap:10px}
.area{flex:1;background:var(--panel);border:1px solid var(--rule);height:270px}
.area h3{background:linear-gradient(var(--green-light),var(--green-dark));color:#fff;font-family:"Oswald",sans-serif;font-weight:400;font-size:14px;text-transform:uppercase;padding:6px 10px;height:42px;line-height:15px}
.area .pic{height:110px;margin:6px 8px;background:linear-gradient(135deg,#d9dccf,#a8ad9d)}
.area p{font-size:10.5px;line-height:1.45;color:var(--muted);padding:0 10px}
.more{display:block;text-align:right;font-size:11px;color:var(--green-dark);font-weight:700;padding:6px 10px}
.welcome{position:absolute;left:38px;top:790px;width:330px}
h2{font-family:"Oswald",sans-serif;font-weight:400;font-size:22px;color:var(--green);text-transform:uppercase}
.welcome .sub{font-size:12px;color:var(--muted);margin-bottom:10px}
.welcome p,.welcome li{font-size:10.5px;line-height:1.5;color:var(--muted)}
.welcome h4{font-size:11px;margin:10px 0 4px;text-transform:uppercase}
.welcome ul{list-style:none}
.welcome li{margin-bottom:5px}
.testimonials{position:absolute;left:405px;top:790px;width:225px}
.quote{font-size:10.5px;line-height:1.5;color:var(--muted);margin-top:8px}
.follow{margin-top:22px}
.social{display:flex;gap:8px;margin-top:8px}
.social i{width:22px;height:22px;border-radius:50%;display:block}
.form{position:absolute;left:660px;top:785px;width:214px;height:300px;background:var(--form-bg);border:1px solid #c4d3b7;padding:8px 10px}
.form h4{text-align:center;font-size:11px;color:var(--muted);font-weight:400;margin-bottom:8px}
.field{height:26px;background:#fff;border:1px solid #c4d3b7;margin-bottom:10px;font-size:10px;color:#999;padding:6px}
.field.area-box{height:110px}
.send{display:block;margin:0 auto;width:130px;height:26px;background:var(--green);color:#fff;font-size:11px;border:none;text-align:center;line-height:26px}
.footer{position:absolute;left:0;top:1115px;width:898px;height:85px;background:var(--footer);color:#ddd}
.footer-links{position:absolute;left:40px;top:18px;font-size:11px}
.footer-links a{color:#ddd;text-decoration:none;margin-right:10px}
.copy{position:absolute;left:40px;top:40px;font-size:10px;color:#999}
.signup{position:absolute;left:680px;top:12px;width:190px}
.signup h5{font-size:12px;font-weight:400;margin-bottom:6px}
.signup div{height:24px;background:#fff;font-size:10px;color:#999;padding:5px}
</style>
</head>
<body>
<header class="header">
  <nav class="nav">
    <a href="#">Home</a><a href="#">About Us</a><a href="#">Associates</a><a href="#">Services</a>
  </nav>
  <div class="brand"><span>VELMORFIELD</span></div>
  <div class="contact">
    <svg width="30" height="30" viewBox="0 0 24 24"><path fill="#3f8a2e" d="M6.6 10.8a15 15 0 0 0 6.6 6.6l2.2-2.2c.3-.3.7-.4 1-.2 1.1.4 2.3.6 3.6.6.6 0 1 .4 1 1V20c0 .6-.4 1-1 1A17 17 0 0 1 3 4c0-.6.4-1 1-1h3.5c.6 0 1 .4 1 1 0 1.3.2 2.5.6 3.6.1.3 0 .7-.2 1z"/></svg>
    <div><div class="cta">Call for a free<br>consultation!</div></div>
    <div class="phone">303-418-7639</div>
  </div>
  <div class="logins">
    <div class="login"><i></i><a href="#">Login</a></div>
    <div class="login"><i></i><a href="#">Login</a></div>
  </div>
  <p class="tagline">"Always do right. This will gratify some people &amp; astonish the rest."</p>
</header>

<section class="slider">
  <div class="slide-photo" role="img" aria-label="Photo of a business advisor in a shirt and tie"></div>
  <h1 class="slide-title">GENERAL FINANCIAL PLANNING</h1>
  <p class="slide-text">Claritas est etiam processus dynamicus, qui sequitur mutationem consuetudium lectorum. Mirum est notare quam littera gothica, quam nunc putamus parum claram.</p>
  <div class="dots"><span>1</span><span>2</span><span>3</span><span>4</span><span>5</span></div>
</section>

<section class="areas">
  <article class="area"><h3>Investment Advice &amp; Education</h3><div class="pic" role="img" aria-label="Photo of financial papers and a pen"></div><p>Lorem ipsum dolor sit amet, consectetuer adipiscing elit, sed diam nonummy nibh euismod tincidunt ut laoreet dolore magna aliquam erat volutpat.</p><a class="more" href="#">Click for more</a></article>
  <article class="area"><h3>General Financial Planning</h3><div class="pic" role="img" aria-label="Photo of advisors at a meeting"></div><p>Lorem ipsum dolor sit amet, consectetuer adipiscing elit, sed diam nonummy nibh euismod tincidunt ut laoreet dolore magna aliquam erat volutpat.</p><a class="more" href="#">Click for more</a></article>
  <article class="area"><h3>Retirement Planning</h3><div class="pic" role="img" aria-label="Photo of a calm retirement scene"></div><p>Lorem ipsum dolor sit amet, consectetuer adipiscing elit, sed diam nonummy nibh euismod tincidunt ut laoreet dolore magna aliquam erat volutpat.</p><a class="more" href="#">Click for more</a></article>
  <article class="area"><h3>401K Planning</h3><div class="pic" role="img" aria-label="Photo of a savings document and calculator"></div><p>Lorem ipsum dolor sit amet, consectetuer adipiscing elit, sed diam nonummy nibh euismod tincidunt ut laoreet dolore magna aliquam erat volutpat.</p><a class="more" href="#">Click for more</a></article>
</section>

<section class="welcome">
  <h2>Welcome Message!</h2>
  <p class="sub">Lorem ipsum dolor sit amet, consectetuer</p>
  <p>Lorem ipsum dolor sit amet, consectetuer adipiscing elit, sed diam nonummy nibh euismod tincidunt ut laoreet dolore magna aliquam erat volutpat. Ut wisi enim ad minim veniam, quis nostrud exerci tation ullamcorper suscipit lobortis nisl ut aliquip ex ea commodo consequat.</p>
  <h4>Services Available:</h4>
  <ul>
    <li>• Facilisis at vero eros et accumsan et iusto odio dignissim qui blandit.</li>
    <li>• Praesent luptatum zzril delenit augue duis dolore te feugait nulla.</li>
    <li>• Nam liber tempor cum soluta nobis eleifend option congue.</li>
    <li>• Duis autem vel eum iriure dolor in hendrerit in vulputate velit esse.</li>
  </ul>
</section>

<section class="testimonials">
  <h2>Testimonials</h2>
  <p class="quote">Lorem ipsum dolor sit amet, consectetuer adipiscing elit, sed diam nonummy nibh euismod.</p>
  <a class="more" href="#">Click more</a>
  <p class="quote">Lorem ipsum dolor sit amet, consectetuer adipiscing elit, sed diam nonummy nibh euismod.</p>
  <a class="more" href="#">Click more</a>
  <div class="follow">
    <h2>Follow Us</h2>
    <div class="social"><i style="background:#3b5998"></i><i style="background:#29a9e1"></i><i style="background:#2a6cb0"></i><i style="background:#5a5a5a"></i><i style="background:#c4302b"></i><i style="background:#f07c1a"></i></div>
  </div>
</section>

<form class="form">
  <h4>Your Message</h4>
  <div class="field">Name</div>
  <div class="field">Email</div>
  <div class="field">Phone</div>
  <div class="field area-box">Your Message</div>
  <div class="send">Send</div>
</form>

<footer class="footer">
  <div class="footer-links"><a href="#">Home</a>|&nbsp; <a href="#">About Us</a>|&nbsp; <a href="#">Contact Us</a></div>
  <p class="copy">Copyright 2013. All rights reserved</p>
  <div class="signup"><h5>News Letter Sign-up</h5><div>Signup here</div></div>
</footer>
</body>
</html>
```